Business Card Design Project

Use newly designed logo and tie into newly designed website
I need a new logo and website layout designed for my partner's business. This is a birthday present. His business is interior painting, wallpapering and design. He also has access to a wide variety of products including carpet, fabrics, furniture, wallpaper, tile, countertops, etc. I have attached some screen shots of his website for reference. He is a one man shop and has a stellar reputation with his customers. He is on-time, very tidy, excellent with animals, and always finishes on time and on budget. There are no restrictions on colors or fonts. The logo needs to work well with the website, business cards and printed materials. The website needs to flow content for device size so it looks just as good on a cell phone or tablet as it does on a desktop computer. Whatever the heck that's called!Thanks. I am looking forward to seeing everyone's ideas.
Target Market(s)
Consumers looking to improve the interior environment of their homes by updating wall paint or paper, flooring (either carpet, tile, or hardwoods), counter tops, window treatments, etc. Clients tend to be more upper middle class and have certain taste levels and expectations. New logo, website and business card should align to meet those levels.
Industry/Entity Type
Cell Phone
Look and feel

```html
<!DOCTYPE html>
<html lang="en">
<head>
<meta charset="utf-8">
<title>Bellamar Interior Designs – Business Card</title>
<link rel="stylesheet" href="https://fonts.googleapis.com/css2?family=Open+Sans:wght@400;600;700&display=swap">
<style>
  :root {
    --backdrop: #a8a8a8;
    --card-white: #ffffff;
    --navy: #1d1a3a;
    --navy-deep: #161430;
    --gold: #a88f5c;
    --gold-light: #b49c68;
    --text-light: #ffffff;
  }
  * { box-sizing: border-box; margin: 0; padding: 0; }
  html, body {
    width: 1200px; height: 900px; overflow: hidden;
    background: var(--backdrop);
    font-family: "Open Sans", "Segoe UI", sans-serif;
  }
  .card {
    position: absolute; left: 120px; top: 170px;
    width: 960px; height: 560px;
    border-radius: 40px; overflow: hidden;
    background: var(--card-white);
    box-shadow: 0 18px 40px rgba(0,0,0,0.25);
  }
  .card-header {
    position: absolute; left: 0; top: 0; width: 100%; height: 262px;
    background: var(--card-white);
  }
  .rule { position: absolute; height: 3px; background: var(--gold); }
  .rule--top-1 { left: 110px; width: 560px; top: 48px; }
  .rule--top-2 { left: 58px; width: 680px; top: 66px; }
  .rule--bottom-1 { left: 58px; width: 680px; top: 206px; }
  .rule--bottom-2 { left: 110px; width: 560px; top: 224px; }
  .brand {
    position: absolute; left: 58px; top: 88px; height: 104px;
    display: flex; align-items: center; gap: 26px;
  }
  .brand-mark {
    width: 96px; height: 96px; background: var(--gold);
  }
  .brand-name {
    font-weight: 700; font-size: 50px; line-height: 1;
    color: var(--navy); letter-spacing: 0.5px;
  }
  .gold-band {
    position: absolute; left: 0; top: 262px; width: 100%; height: 12px;
    background: var(--gold);
  }
  .card-body {
    position: absolute; left: 0; top: 274px; width: 100%; height: 286px;
    background: linear-gradient(180deg, var(--navy) 0%, var(--navy-deep) 100%);
    padding: 22px 0 0 62px;
    color: var(--text-light);
  }
  .person-name {
    font-weight: 700; font-size: 38px; line-height: 1.1; color: var(--gold-light);
  }
  .person-title {
    font-size: 21px; font-weight: 400; margin-top: 2px;
  }
  .contact-list { list-style: none; margin-top: 34px; }
  .contact-item {
    display: flex; align-items: center; gap: 12px;
    font-size: 26px; line-height: 36px;
  }
  .contact-icon { width: 28px; height: 28px; flex: none; fill: var(--gold-light); }
</style>
</head>
<body>
  <main class="card">
    <header class="card-header">
      <div class="rule rule--top-1"></div>
      <div class="rule rule--top-2"></div>
      <div class="brand">
        <div class="brand-mark"></div>
        <h1 class="brand-name">Bellamar Interior Designs</h1>
      </div>
      <div class="rule rule--bottom-1"></div>
      <div class="rule rule--bottom-2"></div>
    </header>
    <div class="gold-band"></div>
    <section class="card-body">
      <h2 class="person-name">Dane Holloway</h2>
      <p class="person-title">Manager</p>
      <ul class="contact-list">
        <li class="contact-item">
          <svg class="contact-icon" viewBox="0 0 24 24" aria-hidden="true"><path d="M6.6 10.8c1.4 2.8 3.8 5.1 6.6 6.6l2.2-2.2c.3-.3.7-.4 1-.2 1.1.4 2.3.6 3.6.6.6 0 1 .4 1 1V20c0 .6-.4 1-1 1C10.6 21 3 13.4 3 4c0-.6.4-1 1-1h3.5c.6 0 1 .4 1 1 0 1.3.2 2.5.6 3.6.1.3 0 .7-.2 1z"/></svg>
          <span>555-310-4826</span>
        </li>
        <li class="contact-item">
          <svg class="contact-icon" viewBox="0 0 24 24" aria-hidden="true"><path d="M12 2a10 10 0 100 20 10 10 0 000-20zm6.9 6h-2.9a15.7 15.7 0 00-1.4-3.6A8 8 0 0118.9 8zM12 4c.8 1.2 1.5 2.5 1.9 4h-3.8c.4-1.4 1.1-2.8 1.9-4zM4.3 14a8.2 8.2 0 010-4h3.4a16.5 16.5 0 000 4zm.8 2h2.9c.3 1.3.8 2.5 1.4 3.6A8 8 0 015.1 16zM8 8H5.1a8 8 0 014.3-3.6C8.8 5.5 8.3 6.7 8 8zm4 12c-.8-1.2-1.5-2.5-1.9-4h3.8c-.4 1.4-1.1 2.8-1.9 4zm2.3-6H9.7a14.7 14.7 0 010-4h4.6a14.7 14.7 0 010 4zm.3 5.6c.6-1.1 1.1-2.3 1.4-3.6h2.9a8 8 0 01-4.3 3.6zm1.7-5.6a16.5 16.5 0 000-4h3.4a8.2 8.2 0 010 4z"/></svg>
          <span>www.bellamardesigns.com</span>
        </li>
        <li class="contact-item">
          <svg class="contact-icon" viewBox="0 0 24 24" aria-hidden="true"><path d="M3 5h18a1 1 0 011 1v12a1 1 0 01-1 1H3a1 1 0 01-1-1V6a1 1 0 011-1zm1 2.2V17h16V7.2l-8 5.3z M4.6 7L12 11.9 19.4 7z"/></svg>
          <span>info@bellamardesigns.com</span>
        </li>
        <li class="contact-item">
          <svg class="contact-icon" viewBox="0 0 24 24" aria-hidden="true"><path d="M12 3l10 9h-3v9h-5v-6h-4v6H5v-9H2z"/></svg>
          <span>48 Linden Hollow Rd. Marlow, NJ. 08610</span>
        </li>
      </ul>
    </section>
  </main>
</body>
</html>
```